Moon River Healing Buisness Cards

I am looking to create a business card for a healing business. In the business I provide coaching and Reiki. I am a licensed LCPC (licensed clinical professional counselor)

Moon River Healing
Soul Centered Healing, Reiki Healinig

Lena Vasquez, L.C.P.C

The card should include the following
biz name: Moon River Healing
my name: Lena Vasquez
website: Lenavasquez.example
email: lena.dorwin@mailbox.example
instagram handle: lenadorwinvasquez

Target Market(s)

Women ages 25-65

```html
<!DOCTYPE html>
<html lang="en">
<head>
<meta charset="utf-8">
<title>Moon River Healing – Business Cards</title>
<link href="https://fonts.googleapis.com/css2?family=Montserrat:wght@400;500;600&display=swap" rel="stylesheet">
<style>
  :root {
    --backdrop: #e4e4e4;
    --navy: #1b1d44;
    --navy-light: #2c2f5c;
    --white: #ffffff;
    --ink: #1f2333;
    --accent: #3f86c8;
    --muted: #444a5a;
  }
  * { margin: 0; padding: 0; box-sizing: border-box; }
  html, body {
    width: 1200px; height: 930px; overflow: hidden;
    background: var(--backdrop);
    font-family: "Montserrat", sans-serif;
  }
  .canvas { position: relative; width: 1200px; height: 930px; }

  .card {
    position: absolute;
    width: 560px; height: 320px;
    border-radius: 18px;
    overflow: hidden;
    box-shadow: 0 6px 18px rgba(0,0,0,0.18);
  }

  /* Front */
  .card-front { left: 90px; top: 110px; background: var(--navy); }
  .card-front .pattern-area {
    position: absolute; inset: 0;
    background: radial-gradient(ellipse at 40% 40%, var(--navy-light) 0%, var(--navy) 75%);
  }
  .card-front .brand-name {
    position: absolute; left: 0; right: 0; top: 50%;
    transform: translateY(-50%);
    text-align: center;
    color: var(--white);
    font-weight: 600; font-size: 38px;
    letter-spacing: 0.5px;
  }

  /* Back */
  .card-back { left: 550px; top: 470px; background: var(--white); }
  .card-back .brand-name {
    position: absolute; left: 90px; top: 70px;
    color: var(--ink);
    font-weight: 600; font-size: 40px;
    letter-spacing: 0.3px;
  }
  .identity {
    position: absolute; right: 310px; top: 190px;
    text-align: right;
  }
  .identity .person-name {
    color: var(--accent);
    font-weight: 500; font-size: 30px; line-height: 1.1;
  }
  .identity .role {
    color: var(--ink); font-size: 15px; margin-top: 4px;
  }
  .divider {
    position: absolute; left: 268px; top: 176px;
    width: 1.5px; height: 98px; background: var(--ink);
  }
  .contact-list {
    position: absolute; left: 286px; top: 168px;
    list-style: none;
    font-size: 15px; color: var(--ink);
  }
  .contact-list li {
    display: flex; align-items: center; gap: 9px;
    height: 27px;
  }
  .contact-list svg { width: 12px; height: 12px; flex: none; }
  .contact-list .highlight { color: var(--accent); }
</style>
</head>
<body>
<div class="canvas">

  <section class="card card-front">
    <div class="pattern-area" role="img" aria-label="Repeating faint star pattern on navy background"></div>
    <div class="brand-name">Moon River Healing</div>
  </section>

  <section class="card card-back">
    <div class="brand-name">Moon River Healing</div>

    <div class="identity">
      <div class="person-name">Lena Vasquez</div>
      <div class="role">Director</div>
    </div>

    <div class="divider"></div>

    <ul class="contact-list">
      <li>
        <svg viewBox="0 0 12 12"><path d="M2.5 1 L4.5 1 L5.2 3.4 L4 4.4 Q5 6.8 7.6 8 L8.6 6.8 L11 7.5 L11 9.5 Q10.5 11 9 11 Q1 10 1 2.5 Q1 1 2.5 1Z" fill="var(--accent)"/></svg>
        +330 555-0142
      </li>
      <li>
        <svg viewBox="0 0 12 12"><rect x="1" y="2.5" width="10" height="7" rx="1" fill="none" stroke="var(--ink)" stroke-width="1.2"/><path d="M1.5 3 L6 6.5 L10.5 3" fill="none" stroke="var(--ink)" stroke-width="1.2"/></svg>
        lena.dorwin@mailbox.example
      </li>
      <li>
        <svg viewBox="0 0 12 12"><circle cx="6" cy="6" r="5" fill="none" stroke="var(--ink)" stroke-width="1.1"/><ellipse cx="6" cy="6" rx="2.2" ry="5" fill="none" stroke="var(--ink)" stroke-width="1"/><path d="M1 6 H11" stroke="var(--ink)" stroke-width="1"/></svg>
        <span>www.<span class="highlight">Lenavasquez</span>.example</span>
      </li>
      <li>
        <svg viewBox="0 0 12 12"><rect x="1.5" y="1.5" width="9" height="9" rx="1.5" fill="var(--ink)"/></svg>
        lenadorwinvasquez
      </li>
    </ul>
  </section>

</div>
</body>
</html>
```